New product NuraLeaf Box Packaging Design

We are looking for a product packaging design concept.

The product name is NuraLeaf, Logo is attached in this post.
NuraLeaf is an infant drop, with probiotic infused with Vitamin D in one. This probiotic + Vitamin D drop is for baby, and it is great for baby's digestive system, and improve immune system.
It is meant for drop per daily use.
It will be in a box, so we are looking for the box design concept.

Although it sounds like a pharmaceutical product, we want the packaging design to look more consumer-friendly, and baby-like.
North American style, modern, and baby product looking, is what we are expecting for this project. Product package needs to visually convey that it is for digestive system & it is for baby.

Some of the brands that has similar concept and products are: Velmora, K Pearls, Hartwell Probiotic Baby, and Quenby's Naturals. Images of the products from these brands are attached for your reference.

We are ONLY looking for the box design for now.
Feel free to contact me for any questions.

Reason: Holiday Season. Office closed. We will be ready to choose the designer in a few days. Thank you!

Baby

Baby

• Our Logo, and baby like design, and visuals that indicate it is great for Baby's digestive system and immune system.

```html
<!DOCTYPE html>
<html lang="en">
<head>
<meta charset="utf-8">
<title>NuraLeaf Infant Drop – Box Front</title>
<link rel="stylesheet" href="https://fonts.googleapis.com/css2?family=Arvo:wght@400;700&family=Bree+Serif&family=Kurale&display=swap">
<style>
  :root {
    --bg: #d9d9d9;
    --white: #ffffff;
    --brand-green: #2aa66a;
    --yellow: #e2d734;
    --lime: #a5c236;
    --blue: #3a87bf;
    --navy: #1e5a96;
    --bubble: #a9d0e6;
    --ink: #1d3b5c;
    --char-green: #25a05a;
    --char-blue: #1f5f9e;
  }
  * { margin: 0; padding: 0; box-sizing: border-box; }
  html, body { width: 873px; height: 1200px; overflow: hidden; }
  body { background: var(--bg); position: relative; }

  .box-front {
    position: absolute; left: 176px; top: 110px;
    width: 520px; height: 980px;
    background: var(--white);
    box-shadow: 0 10px 30px rgba(0,0,0,.18);
    overflow: hidden;
  }
  .bands { position: absolute; inset: 0; width: 520px; height: 980px; }

  .brand {
    position: absolute; left: 0; right: 0; top: 115px;
    display: flex; align-items: center; justify-content: center; gap: 14px;
  }
  .brand-dot { width: 26px; height: 26px; border-radius: 50%; background: var(--brand-green); }
  .brand-name {
    font-family: "Arvo", serif; font-weight: 400; font-size: 60px;
    color: var(--brand-green); line-height: 1;
  }

  .product-title {
    position: absolute; left: 150px; top: 250px;
    font-family: "Arvo", serif; font-weight: 700;
    color: var(--navy); line-height: .85;
  }
  .product-title .line1 { display: block; font-size: 88px; }
  .product-title .line2 { display: block; font-size: 88px; padding-left: 24px; }

  .product-type {
    position: absolute; left: 40px; top: 420px;
    font-family: "Arvo", serif; font-weight: 700; font-size: 50px;
    color: var(--brand-green); line-height: 1;
  }
  .product-extra {
    position: absolute; left: 205px; top: 478px;
    font-family: "Arvo", serif; font-weight: 700; font-size: 34px;
    color: var(--navy); line-height: 1;
  }

  .mascot { position: absolute; border-radius: 48% 48% 42% 42%; }
  .mascot--digest { left: 50px; top: 540px; width: 200px; height: 220px; background: var(--char-green); }
  .mascot--immune { left: 245px; top: 720px; width: 200px; height: 200px; background: var(--char-blue); }

  .bubble {
    position: absolute;
    font-family: "Kurale", serif; font-size: 30px; line-height: 1.05;
    color: var(--ink); text-align: center;
    display: flex; align-items: center; justify-content: center;
  }
  .bubble svg { position: absolute; inset: 0; width: 100%; height: 100%; z-index: 0; }
  .bubble span { position: relative; z-index: 1; }
  .bubble--digest { left: 285px; top: 560px; width: 215px; height: 130px; }
  .bubble--immune { left: 25px; top: 790px; width: 225px; height: 130px; }

  .net-content {
    position: absolute; left: 0; right: 0; bottom: 30px; text-align: center;
    font-family: "Arvo", serif; font-weight: 700; font-size: 20px;
    color: var(--white); letter-spacing: .5px;
  }
</style>
</head>
<body>
  <main class="box-front">
    <svg class="bands" viewBox="0 0 520 980" aria-hidden="true">
      <path fill="var(--yellow)" d="M0 245 C120 215 210 250 300 270 S450 262 520 235 L520 980 L0 980 Z"/>
      <path fill="var(--lime)" d="M0 470 C150 440 290 485 400 470 S480 455 520 440 L520 980 L0 980 Z"/>
      <path fill="var(--blue)" d="M0 715 C130 665 300 670 400 690 S490 700 520 680 L520 980 L0 980 Z"/>
    </svg>

    <div class="brand">
      <span class="brand-dot"></span>
      <span class="brand-name">NuraLeaf</span>
    </div>

    <h1 class="product-title"><span class="line1">infant</span><span class="line2">drop</span></h1>
    <p class="product-type">probiotic</p>
    <p class="product-extra">+ vitamin D</p>

    <div class="mascot mascot--digest" role="img" aria-label="Smiling green drop character with a glowing tummy icon"></div>
    <div class="mascot mascot--immune" role="img" aria-label="Smiling blue drop character flexing its arms"></div>

    <div class="bubble bubble--digest">
      <svg viewBox="0 0 215 130" aria-hidden="true">
        <ellipse cx="115" cy="62" rx="98" ry="58" fill="var(--bubble)"/>
        <path d="M30 90 L0 112 L52 104 Z" fill="var(--bubble)"/>
      </svg>
      <span>good for<br>digestive<br>system</span>
    </div>

    <div class="bubble bubble--immune">
      <svg viewBox="0 0 225 130" aria-hidden="true">
        <ellipse cx="105" cy="66" rx="100" ry="58" fill="var(--bubble)"/>
        <path d="M185 40 L225 22 L200 70 Z" fill="var(--bubble)"/>
      </svg>
      <span>improves<br>immune<br>system</span>
    </div>

    <p class="net-content">90 drops 25 ml (0.08 fl. oz)</p>
  </main>
</body>
</html>
```